QUOTE Graphics for Summer Challenge

I would like to put these quotes over one of the pictures attached; For Instagram, use new size: 4:5 (1080 x 1350 pixels). One Quote per picture, and I want the quote to be bold or easy to read as well. I provided a few reference graphics that I really like as examples below.
All of the pictures are attached; you can pick any photo and add one quote to it; but no stock photography
All the quotes are in the attached WORD document

```html
<!DOCTYPE html>
<html lang="en">
<head>
<meta charset="utf-8">
<title>Sun Girl Summer Reset – Quote Graphics</title>
<link href="https://fonts.googleapis.com/css2?family=Roboto+Condensed:wght@300;400;700&family=Roboto:ital,wght@0,300;0,400;0,700;1,300;1,400;1,700;1,900&display=swap" rel="stylesheet">
<style>
  :root {
    --plum: #7b3a6f;
    --plum-deep: #6e3064;
    --sky: #7cc0e4;
    --sea: #3a9ed6;
    --hills: #8a8a6a;
    --skin: #a8714f;
    --pink: #f2507e;
    --white: #ffffff;
    --page: #ffffff;
  }
  * { margin: 0; padding: 0; box-sizing: border-box; }
  html, body { width: 1200px; height: 3427px; overflow: hidden; background: var(--page); }
  .sheet { position: relative; width: 1200px; height: 3427px; }
  .quote-card {
    position: absolute; width: 467px; height: 583px; overflow: hidden;
    color: var(--white); font-family: "Roboto", Arial, sans-serif;
  }
  .col-left { left: 104px; }
  .col-right { left: 627px; }
  .row-1 { top: 173px; } .row-2 { top: 817px; } .row-3 { top: 1462px; }
  .row-4 { top: 2106px; } .row-5 { top: 2750px; }

  .photo { position: absolute; inset: 0; }
  .photo-portrait-sky { background: linear-gradient(160deg, var(--sky) 0%, #c9a48e 45%, var(--skin) 75%, var(--plum) 100%); }
  .photo-hills { background: linear-gradient(180deg, var(--sky) 0%, #b7d3e2 22%, var(--hills) 40%, var(--skin) 60%, var(--plum) 100%); }
  .photo-pool { background: linear-gradient(180deg, #6f8f5c 0%, var(--sea) 18%, #58b4e6 45%, var(--skin) 70%, var(--plum) 100%); }
  .photo-garden { background: linear-gradient(160deg, #6f9a4f 0%, #9b8f6e 40%, var(--skin) 60%, var(--plum) 100%); }

  .fade-left::after, .fade-bottom::after { content: ""; position: absolute; inset: 0; }
  .fade-left::after { background: linear-gradient(90deg, var(--plum) 30%, rgba(123,58,111,.55) 55%, rgba(123,58,111,0) 80%); }
  .fade-bottom::after { background: linear-gradient(180deg, rgba(123,58,111,0) 35%, rgba(123,58,111,.85) 60%, var(--plum) 72%); }

  .quote { position: absolute; z-index: 2; display: flex; flex-direction: column; line-height: 1.02; }
  .quote.tight { line-height: 0.95; }
  .quote span { display: block; white-space: nowrap; }
  .condensed { font-family: "Roboto Condensed", "Arial Narrow", sans-serif; }
  .it { font-style: italic; }
  .light { font-weight: 300; }
  .bold { font-weight: 700; }
  .pink { color: var(--pink); }
</style>
</head>
<body>
<main class="sheet">

  <section class="quote-card col-left row-1">
    <div class="photo photo-portrait-sky fade-left" role="img" aria-label="Smiling woman with curly hair in a leopard-print bikini, blue sky behind"></div>
    <div class="quote condensed" style="left:18px; top:62px;">
      <span style="font-size:30px;">Feeling bloated,</span>
      <span style="font-size:15px; margin-left:24px;">sluggish, and too big?</span>
      <span class="light" style="font-size:44px;">Your detox</span>
      <span class="bold" style="font-size:42px;">starts now.</span>
      <span style="font-size:30px; margin-left:48px;">Comment</span>
      <span class="bold" style="font-size:62px;">SUMMER</span>
      <span class="light" style="font-size:52px;">to join the</span>
      <span class="bold" style="font-size:46px; margin:18px 0 0 62px;">Sun Girl</span>
      <span class="bold" style="font-size:60px;">Summer</span>
      <span class="light" style="font-size:40px; margin-left:52px;">Reset</span>
    </div>
  </section>

  <section class="quote-card col-right row-1">
    <div class="photo photo-hills fade-bottom" role="img" aria-label="Woman in a dark bikini by an infinity pool with hills behind"></div>
    <div class="quote condensed" style="left:0; right:0; top:375px; align-items:center;">
      <span style="font-size:36px;">The scale keeps climbing</span>
      <span class="pink bold it" style="font-family:Roboto,sans-serif; font-size:27px;">and nothing’s working?</span>
      <span class="light it" style="font-family:Roboto,sans-serif; font-size:27px;">This challenge is your lifeline.</span>
      <span class="it" style="font-family:Roboto,sans-serif; font-size:22px; margin-top:8px;">Comment <b style="font-size:48px; font-weight:400;">SUN GIRL</b></span>
      <span class="pink" style="font-family:Roboto,sans-serif; font-size:27px; margin-left:60px;">to join now!</span>
    </div>
  </section>

  <section class="quote-card col-left row-2">
    <div class="photo photo-portrait-sky fade-left" role="img" aria-label="Woman with curly hair in a crochet fringe swimsuit"></div>
    <div class="quote" style="left:14px; top:106px;">
      <span class="condensed" style="font-size:34px;">Your belly bloat</span>
      <span class="condensed bold pink" style="font-size:54px;">stubborn</span>
      <span class="condensed" style="font-size:26px;">and stubborn weight</span>
      <span class="it" style="font-size:31px; margin-top:6px;">gain aren’t</span>
      <span class="it pink" style="font-size:31px; margin-top:4px;">going anywhere...</span>
      <span class="it" style="font-size:22px; margin-top:6px;">unless you</span>
      <span class="it" style="font-size:22px;">do something different.</span>
      <span class="condensed" style="font-size:24px; margin:4px 0 0 80px;">Comment</span>
      <span class="condensed bold" style="font-size:54px;">SUN GIRL</span>
      <span class="pink" style="font-size:27px; margin-left:50px;">to join now!</span>
    </div>
  </section>

  <section class="quote-card col-right row-2">
    <div class="photo photo-garden fade-bottom" role="img" aria-label="Woman with curly hair posing in front of trees and a modern building"></div>
    <div class="quote it" style="left:52px; top:285px;">
      <span class="bold" style="font-size:36px;">Need a jumpstart?</span>
      <span class="light" style="font-size:36px;">We’re detoxing,</span>
      <span class="light" style="font-size:36px;">burning fat,</span>
      <span class="bold" style="font-size:36px;">and getting snatched.</span>
      <span style="font-size:32px; margin-left:208px;">Comment</span>
      <span style="font-size:54px; margin-left:52px;">SUN GIRL</span>
      <span class="pink" style="font-size:28px; margin-left:30px;">to join us on July 7th</span>
    </div>
  </section>

  <section class="quote-card col-left row-3">
    <div class="photo photo-pool fade-bottom" role="img" aria-label="Woman in sunglasses and a black swimsuit in a blue pool"></div>
    <div class="quote it" style="left:20px; top:224px;">
      <span class="bold" style="font-size:36px;">Cravings,</span>
      <span class="light" style="font-size:36px;">belly fat,</span>
      <span class="light" style="font-size:36px;">and water weight?</span>
      <span class="bold" style="font-size:36px;">Say goodbye in</span>
      <span class="bold" style="font-size:54px; margin-left:74px;">30 days.</span>
      <span style="font-size:32px; margin-left:120px;">Comment</span>
      <span class="bold" style="font-size:54px; margin-left:36px;">SUMMER</span>
      <span class="pink" style="font-size:22px; margin-left:36px;">to join the Sun Girl</span>
      <span style="font-size:38px; margin-left:96px;">Summer Reset</span>
    </div>
  </section>

  <section class="quote-card col-right row-3">
    <div class="photo photo-portrait-sky fade-left" role="img" aria-label="Smiling woman in sunglasses and a black swimsuit"></div>
    <div class="quote it" style="left:38px; top:194px;">
      <span class="bold" style="font-size:36px;">If you feel</span>
      <span class="light" style="font-size:36px;">like you’ve let</span>
      <span class="light" style="font-size:36px;">yourself go lately,</span>
      <span class="bold" style="font-size:36px;">this is your</span>
      <span class="bold" style="font-size:54px;">jumpstart.</span>
      <span style="font-size:32px; margin-left:118px;">Comment</span>
      <span class="bold" style="font-size:54px;">SUMMER</span>
      <span style="font-size:22px; margin-left:70px;">to join the Sun Girl</span>
      <span style="font-size:38px; margin-left:-10px;">Summer Reset</span>
    </div>
  </section>

  <section class="quote-card col-left row-4">
    <div class="photo photo-portrait-sky fade-left" role="img" aria-label="Smiling woman in a leopard-print bikini by the water"></div>
    <div class="quote it" style="left:14px; top:104px;">
      <span class="bold" style="font-size:36px;">Summer’s here,</span>
      <span class="light" style="font-size:36px; margin-left:8px;">but your body</span>
      <span class="light" style="font-size:36px;">doesn’t feel ready?</span>
      <span class="bold" style="font-size:36px; margin-left:58px;">You’re not</span>
      <span class="bold" style="font-size:64px;">too late.</span>
      <span style="font-size:32px; margin-left:100px;">Comment</span>
      <span class="bold" style="font-size:54px;">SUMMER</span>
      <span style="font-size:22px; margin-left:64px;">to join the Sun Girl</span>
      <span style="font-size:38px; margin-left:-4px;">Summer Reset</span>
    </div>
  </section>

  <section class="quote-card col-right row-4">
    <div class="photo photo-pool fade-bottom" role="img" aria-label="Smiling woman in an olive cut-out swimsuit and sheer cover-up by an infinity pool"></div>
    <div class="quote tight it" style="left:0; right:0; top:327px; align-items:center;">
      <span class="light" style="font-size:34px;">This Sun Girl Summer</span>
      <span class="light" style="font-size:34px;">Reset plan is</span>
      <span class="light" style="font-size:34px;">helping women drop pounds</span>
      <span class="bold" style="font-size:54px;">feel sexy again.</span>
      <span style="font-size:28px;">Comment</span>
      <span class="bold" style="font-size:44px;">SUMMER</span>
      <span style="font-size:20px;">to join us</span>
    </div>
  </section>

  <section class="quote-card col-left row-5">
    <div class="photo photo-hills fade-bottom" role="img" aria-label="Woman in an olive cut-out swimsuit posing poolside with hills behind"></div>
    <div class="quote it" style="left:0; right:0; top:326px; align-items:center;">
      <span class="bold" style="font-size:34px;">We’re getting</span>
      <span class="light" style="font-size:34px;">a tiny waist</span>
      <span class="light" style="font-size:32px;">and dropping pounds together.</span>
      <span class="bold" style="font-size:56px;">Don’t miss this.</span>
      <span style="font-size:30px;">Comment</span>
      <span class="bold" style="font-size:48px;">SUN GIRL <small style="font-size:26px; font-weight:400;">to join</small></span>
    </div>
  </section>

  <section class="quote-card col-right row-5">
    <div class="photo photo-hills fade-bottom" role="img" aria-label="Woman in an olive cut-out swimsuit posing with hands on hips, hills behind"></div>
    <div class="quote it" style="left:0; right:0; top:392px; align-items:center;">
      <span class="bold" style="font-size:32px;">You don’t need motivation.</span>
      <span style="font-size:24px;">You need a proven plan and</span>
      <span class="bold" style="font-size:36px;">some accountability.</span>
      <span style="font-size:26px;">Comment <b style="font-size:44px;">SUN GIRL</b></span>
      <span style="font-size:22px;">to get join us July 7th</span>
    </div>
  </section>

</main>
</body>
</html>
```